Vimbalo Food Cafeteria and Food Services

I´m a Mexican Company , I dont know if we can built a US web page, but what we are a Cafeteria and Food Services, basically for industry , we produce food at companies for their employes, I have a Brochure to share if you consider. Our logo was made by your team. We need to have a Web page for our potentials custumers find us easy by internet

Target Market(s)

Food for manufacturers /Industry

Industry/Entity Type

Manufacturer

Number of Pages Required

4 page

Font styles to use
Sans Serif

Requirements
Must have
• Great images, Spanish and English options, our mision , vision , our actual customers , (be able to remove it also), our Certifications, our actual packages for services, our 90 days menu, our catering services, Contact page , Cafeteria Services , our meals serve now .
Nice to have
• Great pics, easy to access , and easy to move into the web page, nutricional ideas.
Should not have
• Fluorescent Color , or brilliant

```html
<!DOCTYPE html>
<html lang="es">
<head>
<meta charset="utf-8">
<title>Vimbalo Food Cafeteria and Food Services</title>
<link rel="stylesheet" href="https://fonts.googleapis.com/css2?family=Roboto:ital,wght@0,300;0,400;0,500;0,700;1,400&display=swap">
<style>
:root{
  --orange:#f07b3f;
  --orange-light:#f5965f;
  --orange-dark:#ea6a2c;
  --green:#3aa935;
  --green-dark:#2b8a2a;
  --ink:#3a2623;
  --grey:#8c8c8c;
  --line:#c9c9c9;
  --white:#ffffff;
  --black:#0d0d0d;
}
*{margin:0;padding:0;box-sizing:border-box}
html,body{width:1200px;height:3159px;overflow:hidden;background:var(--white)}
body{font-family:"Roboto",Arial,sans-serif;color:var(--ink)}
.page{position:relative;width:1200px;height:3159px;overflow:hidden}
.abs{position:absolute}

/* hero */
.hero{position:absolute;left:0;top:0;width:1200px;height:597px;
  background:radial-gradient(ellipse at 20% 40%,#6b4a36 0%,#3b2a20 45%,#1e1410 100%)}
.hero-shade{position:absolute;inset:0;background:linear-gradient(90deg,rgba(120,20,15,.35),rgba(0,0,0,.1) 50%,rgba(140,25,15,.4))}
.brand-box{position:absolute;left:69px;top:0;width:155px;height:146px;background:var(--white);
  display:flex;flex-direction:column;align-items:center;justify-content:center;color:var(--green-dark);font-weight:700}
.brand-name{font-size:34px;line-height:1}
.brand-tag{font-size:10px;margin-top:6px;text-align:center}
.topbar{position:absolute;top:8px;right:70px;display:flex;gap:40px;font-size:13px;color:var(--white);align-items:center}
.topbar span{display:flex;align-items:center;gap:8px}
.nav{position:absolute;top:38px;left:0;font-size:17px;color:var(--white)}
.nav a{position:absolute;white-space:nowrap;color:inherit;text-decoration:none}
.nav .active::after{content:"";position:absolute;left:50%;top:28px;width:18px;height:3px;margin-left:-9px;background:var(--orange)}
.hero-title{position:absolute;left:228px;top:188px;width:400px;text-align:center;color:var(--white);
  font-size:62px;font-weight:700;line-height:50px;letter-spacing:-1px}
.hero-sub{position:absolute;left:238px;top:355px;width:380px;text-align:center;color:var(--white);font-size:14px;line-height:19px}
.btn-outline{position:absolute;border:1.5px solid var(--white);color:var(--white);font-size:15px;
  display:flex;align-items:center;justify-content:center}
.arrow-btn{position:absolute;width:44px;height:64px;background:rgba(0,0,0,.35);display:flex;align-items:center;justify-content:center}
.photo-circle{position:absolute;border-radius:50%}

/* about */
.about{position:absolute;left:0;top:597px;width:1200px;height:470px;
  background:linear-gradient(100deg,var(--orange-dark) 0%,var(--orange) 45%,var(--orange-light) 100%)}
.about h2{position:absolute;left:95px;top:48px;font-size:33px;font-weight:400;color:var(--white)}
.about p{position:absolute;left:95px;width:480px;font-size:15.5px;line-height:20px;color:var(--white);font-weight:300}

.section-title{position:absolute;left:0;width:1200px;text-align:center;font-size:25px;font-weight:500;color:var(--ink)}
.section-title::after{content:"";display:block;width:110px;height:3px;background:var(--green);margin:12px auto 0}

.service-label{position:absolute;width:320px;text-align:center;font-size:21px;line-height:27px;color:var(--ink)}

/* menu cycle */
.cycle{position:absolute;left:0;top:1595px;width:1200px;height:455px;
  background:linear-gradient(100deg,var(--orange-dark) 0%,var(--orange) 50%,var(--orange-light) 100%)}
.cycle-text{position:absolute;left:90px;top:128px;width:420px;font-size:22px;line-height:34px;color:var(--white);font-weight:300}
.step-label{position:absolute;font-size:15px;line-height:19px;color:var(--white)}
.step-label b{font-weight:700}

/* clients */
.client{position:absolute;width:340px;text-align:center}
.client-name{font-size:21px;font-weight:700;color:var(--ink)}
.client-person{font-size:15.5px;color:var(--ink);margin-top:4px}
.client-role{font-size:12px;color:var(--grey);margin-top:1px}
.client-quote{font-size:11.5px;line-height:14.5px;color:var(--grey);font-style:italic;margin:6px auto 0;width:300px}
.slide-btn{position:absolute;width:60px;height:62px;background:#9a9a9a;display:flex;align-items:center;justify-content:center}

/* contact */
.field{position:absolute;left:146px;width:908px;border:1.5px solid var(--line);font-size:11px;color:var(--grey);padding:8px 10px}
.send{position:absolute;left:146px;top:2821px;width:908px;height:32px;background:var(--orange);color:var(--white);
  font-size:16px;font-weight:700;letter-spacing:2px;display:flex;align-items:center;justify-content:center}

/* footer */
.footer{position:absolute;left:0;top:2905px;width:1200px;height:254px;background:var(--black);color:var(--white)}
.footer-brand{position:absolute;left:0;width:1200px;top:30px;text-align:center;font-weight:700}
.footer-nav{position:absolute;top:162px;left:0;width:1200px;display:flex;justify-content:center;gap:40px;font-size:13px}
.footer-addr{position:absolute;top:195px;left:0;width:1200px;text-align:center;font-size:13px;line-height:17px}
.social{position:absolute;top:130px;width:16px;height:16px;border-radius:50%;background:var(--white)}
</style>
</head>
<body>
<div class="page">

  <!-- hero -->
  <section class="hero">
    <div class="hero-shade" role="img" aria-label="Fondo de verduras frescas, chiles y especias sobre mesa oscura"></div>
    <div class="brand-box">
      <div class="brand-name">Vimbalo</div>
      <div class="brand-tag">Cafeteria and Food Services</div>
    </div>
    <div class="topbar">
      <span>
        <svg width="12" height="12" viewBox="0 0 12 12"><path d="M2 1v10M2 1h8l-2 3 2 3H2" fill="#fff" stroke="#fff" stroke-width="1"/></svg>
        Español ⌄
      </span>
      <span>
        <svg width="13" height="13" viewBox="0 0 24 24"><path d="M6.6 10.8a15 15 0 0 0 6.6 6.6l2.2-2.2c.3-.3.7-.4 1-.2 1.1.4 2.3.6 3.6.6.6 0 1 .4 1 1V20c0 .6-.4 1-1 1A17 17 0 0 1 3 4c0-.6.4-1 1-1h3.5c.6 0 1 .4 1 1 0 1.3.2 2.5.6 3.6.1.3 0 .7-.2 1z" fill="#fff"/></svg>
        (686) 555 0142
      </span>
    </div>
    <nav class="nav">
      <a class="active" style="left:455px">Home</a>
      <a style="left:562px">About Us</a>
      <a style="left:700px">Services</a>
      <a style="left:835px">Customers</a>
      <a style="left:985px">Contact Us</a>
    </nav>
    <h1 class="hero-title">Servicios de comedor a empresas</h1>
    <p class="hero-sub">Se proporcionarán los servicios normales de comedor según el menú de la semana y especiales que soliciten dentro de las instalaciones de la empresa.</p>
    <div class="btn-outline" style="left:335px;top:462px;width:157px;height:33px">Más información</div>
    <div class="photo-circle" style="left:613px;top:179px;width:352px;height:352px;border:4px solid #fff;background:radial-gradient(circle at 45% 45%,#e8b24a 0%,#c9c9c0 40%,#8b8f90 75%,#5d6163 100%)" role="img" aria-label="Charolas de servicio con comida caliente"></div>
    <div class="arrow-btn" style="left:34px;top:318px"><svg width="14" height="22" viewBox="0 0 14 22"><path d="M11 2 3 11l8 9" stroke="#fff" stroke-width="2.5" fill="none"/></svg></div>
    <div class="arrow-btn" style="left:1122px;top:318px"><svg width="14" height="22" viewBox="0 0 14 22"><path d="M3 2l8 9-8 9" stroke="#fff" stroke-width="2.5" fill="none"/></svg></div>
  </section>

  <!-- about -->
  <section class="about">
    <h2>Acerca de Nosotros</h2>
    <p style="top:118px">GRUPO ALIMENTA inicia operaciones en Noviembre del 2001 fundamentalmente dando servicio a la empresa Norvia Motors. Como parte de las iniciativas, se inicio un proyecto de servicio de comedores a domicilio con empresas que no cuentan con cocina.</p>
    <p style="top:220px">Grupo Alimenta no sólo piensa en la necesidad de alimentación dentro de las empresas, sino de servicios a domicilio y cafeterías, con personal altamente calificado en dicha área y cocineros expertos en cocina de alta calidad, con la experiencia necesaria para darles el servicio que usted y su personal se merecen.</p>
    <div class="btn-outline" style="left:97px;top:368px;width:157px;height:31px">Leer más</div>
    <div class="photo-circle" style="left:653px;top:56px;width:314px;height:314px;border:4px solid #fff;background:radial-gradient(circle at 50% 50%,#d8452f 0%,#7fae3f 35%,#e9e6dc 70%,#f4f2ec 100%)" role="img" aria-label="Plato de ensalada fresca con tomate y pepino"></div>
    <svg class="abs" style="left:0;top:380px" width="1200" height="90" viewBox="0 0 1200 90">
      <path d="M0 60 C350 55 750 35 1200 0 L1200 90 L0 90Z" fill="#fff"/>
      <path d="M0 92 C350 68 750 50 1200 35" stroke="var(--green)" stroke-width="9" fill="none"/>
    </svg>
  </section>

  <!-- services -->
  <h2 class="section-title" style="top:1078px">Nuestros Servicios</h2>
  <div class="photo-circle" style="left:62px;top:1165px;width:314px;height:314px;border:3px solid var(--green);background:radial-gradient(circle at 50% 55%,#e59a35 0%,#b0602a 45%,#3c2a22 100%)" role="img" aria-label="Buffet de comida caliente servida en charolas"></div>
  <div class="photo-circle" style="left:443px;top:1165px;width:314px;height:314px;border:3px solid var(--green);background:radial-gradient(circle at 50% 60%,#f4f1ec 0%,#cbb9a3 45%,#6b4e38 100%)" role="img" aria-label="Taza de café con galletas"></div>
  <div class="photo-circle" style="left:823px;top:1165px;width:314px;height:314px;border:3px solid var(--green);background:radial-gradient(circle at 50% 60%,#e8c89a 0%,#8a6a55 45%,#2a2730 100%)" role="img" aria-label="Copas de vino y bocadillos para evento"></div>
  <div class="service-label" style="left:59px;top:1512px">Servicios de<br>comedor a empresas</div>
  <div class="service-label" style="left:440px;top:1512px">Servicio de<br>Snack o Cafetería</div>
  <div class="service-label" style="left:820px;top:1512px">Desarrollo de<br>eventos para empresas</div>

  <!-- menu cycle -->
  <section class="cycle">
    <svg class="abs" style="left:0;top:0" width="1200" height="60" viewBox="0 0 1200 60">
      <path d="M0 0 H1200 V22 C800 -2 400 2 0 40Z" fill="#fff"/>
      <path d="M0 36 C400 0 800 -4 1200 20" stroke="var(--green)" stroke-width="9" fill="none"/>
    </svg>
    <p class="cycle-text"><b style="font-weight:700">GRUPO ALIMENTA</b> ofrece menús cíclicos de ocho semanas en los cuales, no se repiten los platillos principales, además de ofrecer otras opciones de alimentación tales como ensaladas, antojitos mexicanos, desayunos y eventualmente se ofrecerá un menú internacional.</p>
    <svg class="abs" style="left:600px;top:40px" width="420" height="400" viewBox="600 1635 420 400" fill="none" stroke="#fff" stroke-width="1.5">
      <circle cx="821" cy="1726" r="55"/>
      <circle cx="925" cy="1828" r="55"/>
      <circle cx="828" cy="1926" r="55"/>
      <circle cx="722" cy="1828" r="55"/>
      <path d="M815 1671 l12 -6 -2 12" />
      <path d="M980 1835 l-8 -12 -8 12"/>
      <path d="M845 1985 l-10 -6 0 12"/>
      <path d="M660 1825 l8 12 8 -12"/>
      <g fill="#fff" stroke="none" font-family="Roboto, Arial, sans-serif" font-size="40" text-anchor="middle">
        <text x="821" y="1740">01</text>
        <text x="925" y="1842">02</text>
        <text x="828" y="1940">03</text>
        <text x="722" y="1842">04</text>
      </g>
    </svg>
    <div class="step-label" style="left:600px;top:0;width:158px;text-align:right;top:-2px;margin-top:0;top:0;transform:translateY(0);" ></div>
    <div class="step-label" style="left:598px;top:-3px;width:160px;text-align:right;margin-top:0;top:0"></div>
    <div class="step-label" style="left:598px;top:0px;width:160px;text-align:right;position:absolute;top:0"></div>
    <div class="step-label" style="left:598px;top:0;width:160px;text-align:right"></div>
    <div class="step-label" style="left:598px;width:160px;text-align:right;top:0"></div>
    <div class="step-label" style="left:598px;width:160px;text-align:right;top:0"></div>
  </section>
  <div class="step-label" style="left:598px;top:1655px;width:160px;text-align:right"><b>8 semanas</b><br>Menú de Arranque<br>y retorno del menú<br>inicial</div>
  <div class="step-label" style="left:936px;top:1678px;width:200px"><b>2do Mes</b><br>Encuesta de servicio y<br>desarrollo de menú<br>según resultados de<br>dicha encuesta.</div>
  <div class="step-label" style="left:560px;top:1872px;width:150px;text-align:right"><b>5to y 6to Mes</b><br>Encuesta<br>nuevo menú<br>según encuestas.</div>
  <div class="step-label" style="left:884px;top:1928px;width:240px"><b>3er Mes</b><br>Nuevo Ciclo de Menú 8 semanas<br>según propuestas del cliente.</div>

  <!-- clients -->
  <h2 class="section-title" style="top:2075px">Nuestros Clientes</h2>
  <div class="slide-btn" style="left:26px;top:2226px"><svg width="12" height="20" viewBox="0 0 12 20"><path d="M10 2 2 10l8 8" stroke="#fff" stroke-width="2" fill="none"/></svg></div>
  <div class="slide-btn" style="left:1114px;top:2226px"><svg width="12" height="20" viewBox="0 0 12 20"><path d="M2 2l8 8-8 8" stroke="#fff" stroke-width="2" fill="none"/></svg></div>
  <div class="photo-circle" style="left:185px;top:2152px;width:146px;height:146px;border:3px solid #e2e2e2;background:linear-gradient(180deg,#d9dde0,#4a5560)" role="img" aria-label="Retrato del representante de Valtera"></div>
  <div class="photo-circle" style="left:527px;top:2152px;width:146px;height:146px;border:3px solid #e2e2e2;background:linear-gradient(180deg,#cfe3ee,#3f4e5e)" role="img" aria-label="Retrato del representante de Norvia Mexicana"></div>
  <div class="photo-circle" style="left:869px;top:2152px;width:146px;height:146px;border:3px solid #e2e2e2;background:linear-gradient(180deg,#e6e6e6,#38465a)" role="img" aria-label="Retrato del representante de Tecnoforma"></div>
  <div class="client" style="left:88px;top:2318px">
    <div class="client-name">VALTERA</div>
    <div class="client-person">Lic. Mateo Ibarra</div>
    <div class="client-role">Gerente de Recursos Humanos</div>
    <p class="client-quote">"El servicio de comedor ha mejorado el ánimo de nuestro personal. Los menús son variados, frescos y siempre llegan a tiempo a cada turno de planta."</p>
  </div>
  <div class="client" style="left:430px;top:2318px">
    <div class="client-name">NORVIA MEXICANA</div>
    <div class="client-person">Lic. Andrés Molina</div>
    <div class="client-role">Gerente de Relaciones Industriales</div>
    <p class="client-quote">"Contamos con su equipo desde hace varios años. La calidad de la comida y la atención del personal de cocina superan lo que esperábamos al iniciar."</p>
  </div>
  <div class="client" style="left:772px;top:2318px">
    <div class="client-name">TECNOFORMA</div>
    <div class="client-person">Lic. Julián Serrano</div>
    <div class="client-role">Recursos Humanos</div>
    <p class="client-quote">"Las encuestas mensuales nos permiten ajustar el menú a nuestros empleados. Es un proveedor serio, atento y muy flexible con los horarios de producción."</p>
  </div>

  <!-- contact -->
  <div class="abs" style="left:60px;top:2505px;width:1080px;height:1px;background:#e4e4e4"></div>
  <h2 class="section-title" style="top:2512px">Contáctenos</h2>
  <div class="field" style="top:2589px;height:43px;padding-top:14px">nombre completo</div>
  <div class="field" style="top:2642px;height:39px;padding-top:12px">email</div>
  <div class="field" style="top:2690px;height:105px">message</div>
  <div class="send">ENVIAR</div>

  <!-- footer -->
  <footer class="footer">
    <div class="footer-brand">
      <div style="font-size:34px;line-height:1">Vimbalo</div>
      <div style="font-size:10px;margin-top:6px">Cafeteria and Food Services</div>
    </div>
    <span class="social" style="left:538px"></span>
    <span class="social" style="left:592px"></span>
    <span class="social" style="left:646px"></span>
    <nav class="footer-nav">
      <span>Home</span><span>About Us</span><span>Services</span><span>Customers</span><span>Contact Us</span>
    </nav>
    <p class="footer-addr">Av. Río Colorado 450 Col. Centro, Mexicali B. C.<br>Tel. (686) 555 0142</p>
  </footer>

</div>
</body>
</html>
```